Looking for an Innovative Print Design (Service Directory)

We need a new design for our advertisement within a printed colour services directory.

We are a compensation law firm called Velbrook Compensation Lawyers. Feel free to take a browse of our website www.velbrooklegal.com.au to get an idea of what we do and the kind of firm we are.

We are in the process of redeveloping our website and as such, so please don't adhere to the design principles of the current site- impress us with your originality!

On top of any editable formats, your final submissions must include a .pdf copy.
The same design will need to be presented in two dimensions:

- 154mm x 118mm (B1/B2 Half Page);
- 175mm x 113mm (B4 Half Page).

[For more information refer to attached Pdf.]

We have attached for you a few examples of other firms' designs (Sample1,2,3). These are by no means good, or what we're after, it's just to provide you with an idea of what sort of advertisements go into the service directory.

Hi all,

We want to emphasise that a priority of the design is that it must look:
• Professional
• Sophisticated
Please do not hesitate to use completely different colour schemes to the ones that are on our website- as we have said, our website will change in the near future, so cohesion between the current project and the website is not necessary!

Thanks!

Thank you for your submissions so far. There are some great ideas hidden in there. 

An issue we are having is that most of you are conforming to the same understanding of what it should look like. Remember that there is NO NEED to be bound by the image of firm as is. That is, feel free to use a different colour logo.

For inspiration, we relate well to the design aesthetics of: http://www.tinfernstudio.co.uk/

Look forward to seeing your 'out of the box' submissions. 

Reason: We've received a large amount of fantastic designs. However, what we're really looking for is something original. Please feel free to think outside the box (the final design doesn't need to look like a print ad), and construct a design that is completely incongruous with our website! While we do appreciate a minimalistic design, we have yet to receive something that really grabs your attention with its visuals. We're not sure but this may or may not be achieved with a full colour design. Thanks for all your submissions- they all have some features that really click with us. We look forward to the next wave of submissions!

Target Market(s)

We have various target markets, including mainly families, elderly people, blue collar workers.

These are individuals who are looking for assistance. They feel helpless or wronged.

Keep in mind that the people accessing these are those who prefer going to a printed directory rather than using a google search.

Industry/Entity Type

Law Firm

Font styles to use
Serif
Sans Serif

Requirements
Must have
• - Our name 'Velbrook Compensation Lawyers'
- Our logo (attached as logo.eps, logo.png, and logo.tif)
- Must include phone number as 1300 XXX XXX (this must be prominent)
- Must include the following service areas in these words: Motor vehicle claims, medical claims, superannuation claims, Workplace claims, negligence claims
- Our email address: info@velbrooklegal.com.au
- Our website address: www.velbrooklegal.com.au
- The following catchphrases: '98% success rate', and 'No win no fee' in those words
- Our location '412 Carvel Lane, Smithville, SYDNEY'
- For sizing dimensions, we need one in 154mm x 118mm and also a design in 175mm x 113mm (B4 Half Page) [refer to pdf attached]
Nice to have
• - Text indicating free initial consulatation
- Professional colour scheme
- As our website will be changed, do not worry about making the advertisement cohesive with our website design
- We want the design to be modern, but still professional
- Clean typeface
- No gradient colour scheme
- When designing, if you are looking to place more text onto the advertisement, these may be some considerations (feel free to change the wording): Accredited specialists, home and hospital visits

```html
<!DOCTYPE html>
<html lang="en">
<head>
<meta charset="utf-8">
<title>Velbrook Compensation Lawyers – Directory Advertisements</title>
<link rel="stylesheet" href="https://fonts.googleapis.com/css2?family=Heebo:wght@300;400;500;700&display=swap">
<style>
  :root {
    --stage: #0b0b0b;
    --brand-blue: #233c99;
    --accent-orange: #f26a21;
    --ink: #3c3c3c;
    --panel-black: #000000;
    --paper: #ffffff;
    --photo-light: #c9c9c9;
    --photo-dark: #1e1e1e;
  }
  * { margin: 0; padding: 0; box-sizing: border-box; }
  html, body {
    width: 1200px; height: 1200px; overflow: hidden;
    background: var(--stage);
    font-family: "Heebo", Arial, sans-serif;
  }
  .sheet { position: relative; width: 1200px; height: 1200px; }

  .size-label {
    position: absolute; color: var(--paper);
    font-style: italic; font-size: 23px; line-height: 30px;
    letter-spacing: 1.5px; text-align: center;
  }
  .size-label--half { left: 205px; top: 56px; width: 300px; }
  .size-label--b4 { left: 740px; top: 1079px; width: 310px; }

  .ad { position: absolute; background: var(--brand-blue); overflow: hidden; }
  .ad--half { left: 538px; top: 32px; width: 621px; height: 636px; }
  .ad--b4 { left: 42px; top: 712px; width: 691px; height: 446px; }

  .headline {
    position: absolute; left: 0; width: 100%;
    color: var(--paper); font-weight: 400; text-align: center; white-space: nowrap;
  }
  .ad--half .headline { top: 15px; font-size: 62px; line-height: 70px; }
  .ad--b4 .headline { top: 18px; font-size: 44px; line-height: 54px; }

  .services-panel {
    position: absolute; background: var(--panel-black);
    border: 2px solid var(--paper); display: flex;
  }
  .ad--half .services-panel { left: 12px; top: 159px; width: 598px; height: 228px; }
  .ad--b4 .services-panel { left: 10px; top: 80px; width: 669px; height: 180px; }

  .services-photo {
    height: 100%; flex: none;
    background: linear-gradient(90deg, var(--photo-dark) 0%, #5a5a5a 30%, var(--photo-light) 55%, #6d6d6d 78%, var(--photo-dark) 100%);
  }
  .ad--half .services-photo { width: 294px; }
  .ad--b4 .services-photo { width: 358px; }

  .service-list { list-style: none; display: flex; flex-direction: column; justify-content: space-between; }
  .ad--half .service-list { margin-left: 20px; padding: 10px 0 11px; }
  .ad--b4 .service-list { margin-left: 17px; padding: 9px 0 9px; }
  .service-item {
    display: flex; align-items: center; gap: 10px;
    color: var(--paper); font-weight: 500; white-space: nowrap;
  }
  .ad--half .service-item { font-size: 21.5px; line-height: 26px; }
  .ad--b4 .service-item { font-size: 22px; line-height: 26px; }
  .service-icon { width: 30px; height: 24px; flex: none; fill: var(--accent-orange); }
  .ad--b4 .service-icon { width: 25px; height: 22px; }

  .contact-panel { position: absolute; }
  .ad--half .contact-panel { left: 12px; top: 394px; width: 598px; height: 205px; }
  .ad--b4 .contact-panel { left: 12px; top: 266px; width: 667px; height: 140px; }
  .contact-panel__shape { position: absolute; left: 0; top: 0; width: 100%; height: 100%; }

  .firm-mark { position: absolute; display: flex; align-items: center; color: var(--ink); font-weight: 400; }
  .firm-mark__dot { border-radius: 50%; background: var(--accent-orange); flex: none; }
  .firm-mark__name { text-transform: uppercase; line-height: 1.1; }
  .firm-mark__name span { display: block; }

  .ad--half .firm-mark { left: 30px; top: 27px; width: 250px; flex-direction: column; gap: 14px; }
  .ad--half .firm-mark__dot { width: 78px; height: 78px; }
  .ad--half .firm-mark__name { text-align: center; font-size: 14px; letter-spacing: 2px; }
  .ad--half .firm-mark__name .firm-mark__lead { font-size: 36px; letter-spacing: 3px; }

  .ad--b4 .firm-mark { left: 16px; top: 17px; gap: 12px; }
  .ad--b4 .firm-mark__dot { width: 72px; height: 72px; }
  .ad--b4 .firm-mark__name { font-size: 13px; letter-spacing: 2px; }
  .ad--b4 .firm-mark__name .firm-mark__lead { font-size: 38px; letter-spacing: 3px; }

  .divider { position: absolute; width: 1px; background: var(--accent-orange); }
  .ad--half .divider { left: 290px; top: 21px; height: 154px; }
  .ad--b4 .divider { left: 352px; top: 12px; height: 96px; }

  .contact { position: absolute; color: var(--ink); white-space: nowrap; }
  .ad--half .contact { left: 316px; top: 14px; }
  .ad--b4 .contact { left: 366px; top: 6px; }
  .contact__title { font-weight: 300; }
  .contact__phone { font-weight: 700; letter-spacing: 0.5px; }
  .contact__line { display: flex; align-items: center; gap: 6px; }
  .contact__line--cont { padding-left: 14px; }
  .contact__icon { width: 8px; height: 9px; fill: var(--accent-orange); flex: none; }

  .ad--half .contact__title { font-size: 33px; line-height: 38px; }
  .ad--half .contact__phone { font-size: 39px; line-height: 44px; }
  .ad--half .contact__line { font-size: 16px; line-height: 21px; }
  .ad--b4 .contact__title { font-size: 24px; line-height: 28px; }
  .ad--b4 .contact__phone { font-size: 27px; line-height: 29px; }
  .ad--b4 .contact__line { font-size: 12px; line-height: 16px; }

  .tagline {
    position: absolute; left: 0; width: 100%;
    color: var(--paper); font-weight: 300; text-align: center; white-space: nowrap;
  }
  .ad--half .tagline { top: 597px; font-size: 20px; line-height: 26px; }
  .ad--b4 .tagline { top: 408px; font-size: 22px; line-height: 28px; }
</style>
</head>
<body>
<svg width="0" height="0" style="position:absolute" aria-hidden="true">
  <defs>
    <symbol id="icon-car" viewBox="0 0 30 24">
      <path d="M7 3h16l4 8h2v9h-4v3h-4v-3H9v3H5v-3H1v-9h2zM9 6l-2.5 5h17L21 6z"/>
      <circle cx="7" cy="15" r="2" fill="#000"/><circle cx="23" cy="15" r="2" fill="#000"/>
    </symbol>
    <symbol id="icon-medical" viewBox="0 0 30 24">
      <path d="M10 2h10v4h-2V4h-6v2h-2zM2 6h26a2 2 0 0 1 2 2v13a2 2 0 0 1-2 2H2a2 2 0 0 1-2-2V8a2 2 0 0 1 2-2z"/>
      <path d="M13 9h4v4h4v4h-4v4h-4v-4H9v-4h4z" fill="#000"/>
    </symbol>
    <symbol id="icon-savings" viewBox="0 0 30 24">
      <circle cx="18" cy="5" r="4.5"/>
      <ellipse cx="15" cy="15" rx="11" ry="7"/>
      <rect x="7" y="19" width="4" height="5"/><rect x="19" y="19" width="4" height="5"/>
      <rect x="1" y="12" width="4" height="4"/>
    </symbol>
    <symbol id="icon-workplace" viewBox="0 0 30 24">
      <path d="M2 2h3v8h8v3H5v11H2zM14 8h14v3h-2v13h-3V15h-6v9h-3V11h0z"/>
      <rect x="7" y="4" width="5" height="4"/>
    </symbol>
    <symbol id="icon-warning" viewBox="0 0 30 24">
      <path d="M15 1 29 23H1zM15 5.5 4.8 21h20.4z"/>
      <rect x="13.8" y="9" width="2.4" height="7"/><rect x="13.8" y="17.5" width="2.4" height="2.4"/>
    </symbol>
    <symbol id="icon-globe" viewBox="0 0 8 9"><circle cx="4" cy="4.5" r="3.8"/></symbol>
    <symbol id="icon-mail" viewBox="0 0 8 9"><rect x="0" y="2" width="8" height="5.5"/></symbol>
    <symbol id="icon-pin" viewBox="0 0 8 9"><path d="M4 0a3 3 0 0 1 3 3c0 2.2-3 6-3 6S1 5.2 1 3a3 3 0 0 1 3-3z"/></symbol>
  </defs>
</svg>

<main class="sheet">
  <p class="size-label size-label--half">154mm x 118mm<br>(B1/B2 Half Page)</p>

  <section class="ad ad--half" aria-label="Velbrook Compensation Lawyers half page advertisement">
    <h1 class="headline">No win no fee.<br>98% success rate!</h1>
    <div class="services-panel">
      <div class="services-photo" role="img" aria-label="Photograph of two businessmen in suits shaking hands"></div>
      <ul class="service-list">
        <li class="service-item"><svg class="service-icon"><use href="#icon-car"/></svg>Motor vehicle claims</li>
        <li class="service-item"><svg class="service-icon"><use href="#icon-medical"/></svg>Medical claims</li>
        <li class="service-item"><svg class="service-icon"><use href="#icon-savings"/></svg>Superannuation claims</li>
        <li class="service-item"><svg class="service-icon"><use href="#icon-workplace"/></svg>Workplace claims</li>
        <li class="service-item"><svg class="service-icon"><use href="#icon-warning"/></svg>Negligence claims</li>
      </ul>
    </div>
    <div class="contact-panel">
      <svg class="contact-panel__shape" viewBox="0 0 598 205" preserveAspectRatio="none" aria-hidden="true">
        <path d="M0 0H598V175Q299 207 0 175Z" fill="#fff"/>
        <path d="M0 184Q299 216 598 184" fill="none" stroke="#fff" stroke-width="2"/>
      </svg>
      <div class="firm-mark">
        <span class="firm-mark__dot"></span>
        <p class="firm-mark__name"><span class="firm-mark__lead">Velbrook</span><span>Compensation Lawyers</span></p>
      </div>
      <span class="divider"></span>
      <div class="contact">
        <p class="contact__title">Contact Us Today!</p>
        <p class="contact__phone">1300 XXX XXX</p>
        <p class="contact__line"><svg class="contact__icon"><use href="#icon-globe"/></svg>www.velbrooklegal.com.au</p>
        <p class="contact__line"><svg class="contact__icon"><use href="#icon-mail"/></svg>info@velbrooklegal.com.au</p>
        <p class="contact__line"><svg class="contact__icon"><use href="#icon-pin"/></svg>412 Carvel Lane</p>
        <p class="contact__line contact__line--cont">Smithville, Sydney</p>
      </div>
    </div>
    <p class="tagline">Accredited specialists, home and hospital visits.</p>
  </section>

  <section class="ad ad--b4" aria-label="Velbrook Compensation Lawyers B4 half page advertisement">
    <h1 class="headline">No win no fee. 98% success rate!</h1>
    <div class="services-panel">
      <div class="services-photo" role="img" aria-label="Photograph of two businessmen in suits shaking hands"></div>
      <ul class="service-list">
        <li class="service-item"><svg class="service-icon"><use href="#icon-car"/></svg>Motor vehicle claims</li>
        <li class="service-item"><svg class="service-icon"><use href="#icon-medical"/></svg>Medical claims</li>
        <li class="service-item"><svg class="service-icon"><use href="#icon-savings"/></svg>Superannuation claims</li>
        <li class="service-item"><svg class="service-icon"><use href="#icon-workplace"/></svg>Workplace claims</li>
        <li class="service-item"><svg class="service-icon"><use href="#icon-warning"/></svg>Negligence claims</li>
      </ul>
    </div>
    <div class="contact-panel">
      <svg class="contact-panel__shape" viewBox="0 0 667 140" preserveAspectRatio="none" aria-hidden="true">
        <path d="M0 0H667V100Q333.5 136 0 100Z" fill="#fff"/>
        <path d="M0 108Q333.5 144 667 108" fill="none" stroke="#fff" stroke-width="2"/>
      </svg>
      <div class="firm-mark">
        <span class="firm-mark__dot"></span>
        <p class="firm-mark__name"><span class="firm-mark__lead">Velbrook</span><span>Compensation Lawyers</span></p>
      </div>
      <span class="divider"></span>
      <div class="contact">
        <p class="contact__title">Contact Us Today!</p>
        <p class="contact__phone">1300 XXX XXX</p>
        <p class="contact__line"><svg class="contact__icon"><use href="#icon-globe"/></svg>www.velbrooklegal.com.au</p>
        <p class="contact__line"><svg class="contact__icon"><use href="#icon-mail"/></svg>info@velbrooklegal.com.au</p>
        <p class="contact__line"><svg class="contact__icon"><use href="#icon-pin"/></svg>412 Carvel Lane, Smithville, Sydney</p>
      </div>
    </div>
    <p class="tagline">Accredited specialists, home and hospital visits.</p>
  </section>

  <p class="size-label size-label--b4">175mm x 113mm<br>(B4 Half Page)</p>
</main>
</body>
</html>
```